ベースの色はグリーンですが、その系統の配色か、必要に応じては青をいれてもらってもかまいません。コーポレートサイトのデザインですが、色々な方のパターンを見てみたいです。
採用も目的としているため比較的爽やかなイメージが良いかもしれません。
仕様書【ミライワークス用】.pdfと添付画像をもとにデザイン作成お願いします。

当選前提となった方は正式な社名及び連絡先をお伝えしますので修正対応をお願いします。
また希望の際は、当選後、中ページの制作及びコーディングも別途ご依頼可能です。
ページ数
1ページ
希望イメージ
シンプル 複雑
単色 カラフル
暗い 明るい
日常 高級
遊び心 厳粛
未来的 伝統的
女性的 男性的
希望する色
緑系、青系
納品ファイル
• 高解像度JPG (.jpg)
• フォトショップ形式 (.psd)
弊社で納品している運送系サイトを参考までに記載します。

https://www.harunomiya.co.jp/
https://www.mido-hakobi.co.jp/
https://www.tachibe-web.co.jp/
https://www.renkaru.net/
■ 選んだ理由

採用を意識したイメージと、全体のメリハリ感が非常にマッチしておりました。
ありがとうございます。

■ 提案者全員のお礼・コメント

たくさんのご提案ありがとうございます。
どれも非常にレベルが高く弊社デザイナー感でも意見が割れて迷いました。
またの機会がありましたらよろしくお願いいたします。

```html
<!DOCTYPE html>
<html lang="ja">
<head>
<meta charset="utf-8">
<title>株式会社ミナト運送</title>
<link href="https://fonts.googleapis.com/css2?family=Noto+Serif+JP:wght@400;500;700&family=Noto+Sans+JP:wght@400;500;700&family=Cormorant+Garamond:wght@400;500&display=swap" rel="stylesheet">
<style>
:root{
  --green:#1f9a45;
  --green-deep:#147a35;
  --green-dark:#0e3d22;
  --ink:#2b2b2b;
  --white:#ffffff;
  --footer:#161a17;
  --line:#e4e4e4;
}
*{box-sizing:border-box;margin:0;padding:0}
html,body{width:1200px;height:3232px;overflow:hidden}
body{position:relative;background:var(--white);font-family:"Noto Sans JP",sans-serif;color:var(--ink)}
.abs{position:absolute}
.serif{font-family:"Noto Serif JP",serif}
.latin{font-family:"Cormorant Garamond",serif}

/* header */
.brand{left:40px;top:36px;display:flex;align-items:center;gap:12px;z-index:5}
.brand-dot{width:30px;height:30px;border-radius:50%;background:var(--green)}
.brand-name{font-family:"Noto Serif JP",serif;font-weight:700;font-size:19px;color:var(--ink);line-height:1.1}
.brand-sub{font-size:10px;color:var(--ink);letter-spacing:.05em}
.nav{left:440px;top:0;width:760px;height:72px;background:var(--green);display:flex;align-items:center;justify-content:flex-end;z-index:5}
.nav a{color:var(--white);text-decoration:none;text-align:center;font-size:14px;margin-right:38px;line-height:1.2}
.nav a small{display:block;font-size:8px;opacity:.8}
.nav .nav-btn{width:72px;height:72px;margin:0;display:flex;flex-direction:column;align-items:center;justify-content:center;gap:4px;font-size:9px;background:var(--green-deep)}
.nav .nav-btn.mail{background:var(--green-dark)}

/* hero */
.hero-circle{left:-260px;top:-120px;width:700px;height:700px;border-radius:50%;background:#f3f7f3}
.hero-green{left:0;top:160px;width:410px;height:1000px;background:var(--green)}
.hero-photo{left:400px;top:72px;width:800px;height:630px;background:linear-gradient(135deg,#cfe3f2 0%,#e8eef2 40%,#4a6fb7 70%,#d9dde2 100%)}
.hero-leaf{left:400px;top:72px;width:270px;height:230px;background:linear-gradient(160deg,#7dc45a,#2f8c3a)}
.hero-copy{left:40px;top:420px;color:var(--white);font-size:62px;line-height:1.2;font-weight:400;z-index:3}

/* business */
.biz-vert{left:424px;top:730px;writing-mode:vertical-rl;font-size:20px;color:var(--green);letter-spacing:.3em;z-index:3}
.biz-card{left:470px;top:700px;width:730px;height:460px;background:var(--white);padding:40px 0 0 60px}
.biz-title{font-size:34px;color:var(--green);line-height:1.55;font-weight:500;letter-spacing:.08em}
.biz-text{margin-top:26px;font-size:13px;line-height:2.6;color:#555}
.btn{display:inline-flex;align-items:center;justify-content:space-between;gap:18px;border:1px solid var(--green);color:var(--green);font-size:13px;padding:12px 22px;background:var(--white);text-decoration:none}
.btn svg{width:22px;height:8px}
.biz-card .btn{position:absolute;right:140px;bottom:130px}
.ness{left:-30px;top:1040px;font-size:200px;line-height:1;color:var(--white);font-family:"Cormorant Garamond",serif;z-index:2}

/* building band */
.band-photo{left:0;top:1160px;width:1200px;height:520px;background:linear-gradient(180deg,#cfdfee 0%,#e7edf1 35%,#f4f4f4 60%,#9fb1bf 100%)}
.cards{left:120px;top:1320px;width:960px;display:flex;gap:22px;z-index:2}
.card{flex:1;height:200px;background:var(--white);padding:26px 24px;border:1px solid var(--line)}
.card h3{font-family:"Noto Serif JP",serif;font-size:15px;font-weight:500;color:var(--ink)}
.card p{font-size:11px;color:var(--green);margin-top:4px}
.card .btn{margin-top:64px;width:180px;font-size:12px;padding:9px 18px;margin-left:60px}

/* recruit */
.recruit{left:0;top:1560px;width:1200px;height:1000px;background:var(--green)}
.recruit-circle{left:-200px;top:1520px;width:500px;height:500px;border-radius:50%;background:rgba(255,255,255,.05)}
.recruit-title{left:120px;top:1630px;color:var(--white);font-size:44px;line-height:1.6;letter-spacing:.08em;font-weight:500}
.recruit-text{left:120px;top:1830px;color:var(--white);font-size:13px;line-height:2.6}
.recruit-btn{left:120px;top:1960px;background:transparent;border-color:var(--white);color:var(--white)}
.people{left:680px;top:1720px;width:520px;height:840px;background:linear-gradient(180deg,#f2f5f8 0%,#d9e2ea 30%,#2b58b0 55%,#203f86 100%)}
.truck{left:120px;top:2090px;width:560px;height:470px;background:linear-gradient(160deg,#f3f4f5 0%,#d3d7db 55%,#6f7780 100%)}

/* contact */
.contact-bg{left:0;top:2560px;width:1200px;height:480px;background:radial-gradient(ellipse at 30% 40%,#2f6b3a 0%,#163b22 55%,#0f2617 100%)}
.contact-box{left:120px;top:2635px;width:960px;height:250px;border:1px solid rgba(255,255,255,.8);display:flex;color:var(--white)}
.contact-box > div{display:flex;flex-direction:column;justify-content:center;padding:0 36px}
.contact-box > .c-head{width:300px}
.contact-box > .c-tel{width:330px;border-left:1px solid rgba(255,255,255,.5)}
.contact-box > .c-mail{flex:1;border-left:1px solid rgba(255,255,255,.5)}
.contact-head{font-family:"Noto Serif JP",serif;font-size:17px}
.contact-head small{display:block;font-size:11px;opacity:.8;margin-top:4px;font-family:"Noto Sans JP",sans-serif}
.contact-label{font-size:12px;margin-bottom:20px}
.tel{font-size:26px;font-family:"Noto Serif JP",serif;letter-spacing:.03em;white-space:nowrap}
.tel small{font-size:13px;margin-right:10px}
.mail-btn{background:var(--white);color:var(--green-dark);font-size:13px;padding:12px 20px;width:200px;display:flex;justify-content:space-between;align-items:center;text-decoration:none}

/* footer */
.footer{left:0;top:3040px;width:1200px;height:192px;background:var(--footer)}
.footer-brand{left:120px;top:3070px;display:flex;align-items:center;gap:12px}
.footer-brand .brand-dot{background:var(--white)}
.footer-brand .brand-name,.footer-brand .brand-sub{color:var(--white)}
.footer-addr{left:120px;top:3130px;font-size:10px;line-height:1.8;color:#bbb}
.footer-nav{left:640px;top:3070px;display:flex;gap:22px;font-size:11px;color:var(--white)}
.footer-sub{left:790px;top:3104px;display:flex;gap:22px;font-size:10px;color:#bbb}
.copy{left:880px;top:3200px;font-size:9px;color:#999}
</style>
</head>
<body>

<div class="abs hero-circle"></div>
<div class="abs hero-green"></div>
<div class="abs hero-photo" role="img" aria-label="青と白の大型トラックが並ぶ写真"></div>
<div class="abs hero-leaf" role="img" aria-label="明るい緑の葉の写真"></div>

<div class="abs brand"><span class="brand-dot"></span><div><div class="brand-name">株式会社ミナト運送</div><div class="brand-sub">Minato Unso Inc.</div></div></div>

<nav class="abs nav">
  <a href="#">Home<small>ホーム</small></a>
  <a href="#">Business<small>事業内容</small></a>
  <a href="#">Environment<small>環境・品質方針</small></a>
  <a href="#">Vehicle<small>車両案内</small></a>
  <a href="#">Company<small>会社案内</small></a>
  <a href="#" class="nav-btn">
    <svg width="18" height="18" viewBox="0 0 18 18" fill="none" stroke="#fff" stroke-width="1.6"><circle cx="9" cy="6" r="3.5"/><path d="M2 17c1-4 4-5.5 7-5.5s6 1.5 7 5.5"/></svg>採用情報</a>
  <a href="#" class="nav-btn mail">
    <svg width="20" height="16" viewBox="0 0 20 16" fill="none" stroke="#fff" stroke-width="1.6"><rect x="1" y="1" width="18" height="14"/><path d="M1 1l9 8 9-8"/></svg>お問い合わせ</a>
</nav>

<div class="abs hero-copy latin">Safety<br>Relief<br>Reliability</div>

<section class="abs biz-card">
  <h2 class="biz-title serif">安全・安心・信頼される<br>企業として</h2>
  <p class="biz-text">日々の輸送を通じて地域の暮らしと産業を支え、お客様に信頼される運送会社を目指します。<br>私たちは安全を第一に、確かな品質で大切な荷物をお届けします。</p>
  <a href="#" class="btn">事業内容について <svg viewBox="0 0 22 8" fill="none" stroke="currentColor"><path d="M0 7h21l-6-6"/></svg></a>
</section>
<div class="abs biz-vert serif">事業内容</div>

<div class="abs band-photo" role="img" aria-label="白い倉庫の建物と青空の写真"></div>
<div class="abs ness">ness</div>
<div class="abs cards">
  <div class="card"><h3>環境・品質方針</h3><p>Environment</p><a href="#" class="btn">詳しく見る <svg viewBox="0 0 22 8" fill="none" stroke="currentColor"><path d="M0 7h21l-6-6"/></svg></a></div>
  <div class="card"><h3>車両案内</h3><p>Vehicle</p><a href="#" class="btn">詳しく見る <svg viewBox="0 0 22 8" fill="none" stroke="currentColor"><path d="M0 7h21l-6-6"/></svg></a></div>
  <div class="card"><h3>会社案内</h3><p>Company</p><a href="#" class="btn">詳しく見る <svg viewBox="0 0 22 8" fill="none" stroke="currentColor"><path d="M0 7h21l-6-6"/></svg></a></div>
</div>

<div class="abs recruit"></div>
<div class="abs recruit-circle"></div>
<h2 class="abs recruit-title serif">私たちと一緒に、<br>運びませんか？</h2>
<p class="abs recruit-text">ミナト運送は、一緒に働く仲間を募集しています。<br>未経験の方も安心して始められるよう、研修制度を整えています。</p>
<a href="#" class="abs btn recruit-btn">採用情報について <svg viewBox="0 0 22 8" fill="none" stroke="currentColor"><path d="M0 7h21l-6-6"/></svg></a>
<div class="abs truck" role="img" aria-label="白いトラックの運転席まわりの写真"></div>
<div class="abs people" role="img" aria-label="青い作業着と帽子のドライバー二人の写真"></div>

<div class="abs contact-bg" role="img" aria-label="ぼかした緑の木々の背景写真"></div>
<section class="abs contact-box">
  <div class="c-head"><p class="contact-head">お問い合わせ<small>Contact</small></p></div>
  <div class="c-tel"><p class="contact-label">お電話のお問い合わせ</p><p class="tel"><small>TEL</small>012-3456-7890</p></div>
  <div class="c-mail"><p class="contact-label">メールでのお問い合わせ</p><a href="#" class="mail-btn">お問い合わせ <svg width="22" height="8" viewBox="0 0 22 8" fill="none" stroke="currentColor"><path d="M0 7h21l-6-6"/></svg></a></div>
</section>

<footer class="abs footer"></footer>
<div class="abs footer-brand"><span class="brand-dot"></span><div><div class="brand-name">株式会社ミナト運送</div><div class="brand-sub">Minato Unso Inc.</div></div></div>
<p class="abs footer-addr">〒000-0000<br>緑ヶ丘市港町1丁目2番3号</p>
<div class="abs footer-nav"><span>ホーム</span><span>事業内容</span><span>環境・品質方針</span><span>車両案内</span><span>会社案内</span><span>採用情報</span><span>お問い合わせ</span></div>
<div class="abs footer-sub"><span>プライバシーポリシー</span><span>サイトマップ</span><span>関連情報</span></div>
<p class="abs copy">Copyright©2024 All Right Reserved.</p>

</body>
</html>
```